THE TALL COPPER ATLAS OF PORTS

subtitle: AN INTRO TO SEARCH ENGINE OPTIMIZATION
background: white
dimensions: 1562x2500

Target Market(s)

Marketing professionals

Industry/Entity Type

Digital Marketing

Font styles to use
Sans Serif

Colors
ffffff
1b1b1b
3176b5

Requirements
Should not have
• Images or graphics

```html
<!DOCTYPE html>
<html lang="en">
<head>
<meta charset="utf-8">
<title>The Tall Copper Atlas of Ports – Book Cover</title>
<link rel="stylesheet" href="https://fonts.googleapis.com/css2?family=Arimo:wght@700&family=Roboto+Condensed:wght@700&display=swap">
<style>
  :root {
    --paper: #ffffff;
    --ink: #1b1b1b;
    --accent: #3176b5;
    --author-tint: #c4dfe2;
    --stage: #ececec;
  }
  * { margin: 0; padding: 0; box-sizing: border-box; }
  html, body {
    width: 1200px;
    height: 789px;
    overflow: hidden;
    background: var(--stage);
  }
  .stage {
    width: 1200px;
    height: 789px;
    display: flex;
    align-items: center;
    justify-content: center;
  }
  .cover {
    position: relative;
    width: 462px;
    height: 740px;
    background: var(--paper);
    overflow: hidden;
  }
  .cover-title {
    position: absolute;
    left: 26px;
    top: 34px;
    font-family: "Arimo", "Helvetica Neue", Arial, sans-serif;
    font-weight: 700;
    color: var(--ink);
    text-transform: uppercase;
    white-space: nowrap;
  }
  .cover-title span { display: block; }
  .title-small {
    font-size: 70px;
    line-height: 0.9;
    letter-spacing: -1px;
  }
  .title-large {
    font-size: 94px;
    line-height: 0.9;
    letter-spacing: -3px;
  }
  .title-topic {
    margin-top: 8px;
    font-size: 120px;
    line-height: 0.88;
    letter-spacing: -4px;
    color: var(--accent);
  }
  .cover-subtitle {
    position: absolute;
    left: 28px;
    top: 476px;
    font-family: "Arimo", "Helvetica Neue", Arial, sans-serif;
    font-weight: 700;
    font-size: 21px;
    line-height: 1.2;
    color: var(--ink);
    text-transform: uppercase;
  }
  .author-band {
    position: absolute;
    left: 0;
    right: 0;
    bottom: 0;
    height: 172px;
    background: var(--ink);
    display: flex;
    align-items: flex-end;
    padding: 0 0 38px 28px;
  }
  .author-name {
    font-family: "Roboto Condensed", "Arial Narrow", sans-serif;
    font-weight: 700;
    font-size: 66px;
    line-height: 1;
    color: var(--author-tint);
    text-transform: uppercase;
    white-space: nowrap;
  }
</style>
</head>
<body>
  <main class="stage">
    <article class="cover">
      <h1 class="cover-title">
        <span class="title-small">The Tall</span>
        <span class="title-large">Copper</span>
        <span class="title-large">Atlas</span>
        <span class="title-small">Of</span>
        <span class="title-topic">Ports</span>
      </h1>
      <p class="cover-subtitle">An Intro to Search Engine<br>Optimization</p>
      <footer class="author-band">
        <p class="author-name">Author Name</p>
      </footer>
    </article>
  </main>
</body>
</html>
```